Modern, upmarket label design for food product

We need a label design for a food company producing nuts with sesame and honey. In fact, we would like the words "Cashews med sesam & honning" on the label (It's in Danish and means - Cashews with sesame & honey). It should be easy for the customer to quickly understand what it is.

It is a shelf product in the competitive food industry, which is why the design should wake the feeling of 'just wanting to grab the product down from the shelves'. So, the design should stand out and have an image of a cool, modern, hip product. This being said, I love a raw & handmade look.

The company is called Tyvo. Its origins are from the danish word Pilt that is a Danish slang for yummy. I have uploaded a photo of the package the products will be sold in.

Info & dimensions on bag in picture 1.
Dimensions: 6" x 9" | 15.2 cm x 22.3 cm
Capacity: 8 ounces | 250 grams (based on whole bean coffee)

Picture 2 is the same product, but has the possibility of attaching to a hanger on shelfs.

Picture 3 - I have also uploaded a photo of a product bag, where the hole is linear instead of a round hole. The designer chooses, which bag they will like to work with!

Please let me know if there are any questions!

Target Market(s)

Target market could really be any age, but the design needs to compel the target audience to pick it from the shelves. The package should signal a product you want to hold and have other people seeing you have it. The target audience is people who cares for what they buy, and typically doesn't want a low-end or budget product. They want the whole thing, meaning it has to taste good, look good etc. They are also the type of people who like to show off whatever products they buy by placing them in their houses for their guests to see. Or by uploading pictures of it on social medias.

Industry/Entity Type

It Company

Font styles to use
Other font styles liked:
• Not a must, but I like the 'Panton' script

Requirements
Must have
• My project must have the words 'Cashews med sesam & honning' on the label, so the customer will know within a second what they are looking at and buying.
Nice to have
• I am picturing the label with the words 'Cashews med sesam & honning' as a statement, again, emphasizing how the customer instantly should know what the product is. This being said, it should not be the only thing on the package and I love a raw & handmade look - which inspiration picture 5 is a great example of!
• I have uploaded photos of what I think looks good. With this said, I am not looking for a copy of those products, but see them as good inspiration. I have named the photos inspiration 1, 2, 3, 4 & 5.
• If needed, more text can be put on the label. For example 'vegan', 'laktosefri', Glutenfri', or 'Sund Snack' are great words for being used on the label.
Should not have
• The fonts on the label should not be too decorative. Personally I like an easy too read font.

```html
<!DOCTYPE html>
<html lang="da">
<head>
<meta charset="utf-8">
<title>Cashews med sesam &amp; honning – label</title>
<link rel="stylesheet" href="https://fonts.googleapis.com/css2?family=Anton&family=Comic+Neue:wght@700&family=Arimo:wght@400;700&display=swap">
<style>
  :root {
    --page-bg: #ffffff;
    --label-cream: #e3d6a9;
    --pattern-tone: #ebe0bb;
    --ink: #111111;
    --paper-white: #ffffff;
    --ribbon-shade: #f2f0ea;
  }
  html, body {
    margin: 0;
    padding: 0;
    width: 1200px;
    height: 1005px;
    overflow: hidden;
    background: var(--page-bg);
  }
  .canvas {
    position: relative;
    width: 1200px;
    height: 1005px;
  }
  .label {
    position: absolute;
    left: 370px;
    top: 271px;
    width: 460px;
    height: 463px;
  }
  .label-edge { fill: var(--label-cream); }
  .label-pattern { fill: url(#patternTone); }
  .headline {
    font-family: "Anton", "Oswald", sans-serif;
    fill: var(--ink);
  }
  .connector {
    font-family: "Arimo", Arial, sans-serif;
    fill: var(--paper-white);
  }
  .ampersand {
    font-family: "Arimo", Arial, sans-serif;
    font-weight: 700;
    fill: var(--paper-white);
  }
  .ribbon-band { fill: var(--paper-white); }
  .ribbon-fold { fill: var(--ribbon-shade); }
  .claims {
    font-family: "Comic Neue", "Comic Sans MS", cursive;
    font-weight: 700;
    fill: var(--ink);
  }
  .maker-line {
    font-family: "Arimo", Arial, sans-serif;
    fill: var(--paper-white);
  }
  .brand-name {
    font-family: "Arimo", Arial, sans-serif;
    fill: var(--ink);
    letter-spacing: 1px;
  }
</style>
</head>
<body>
<main class="canvas">
  <svg class="label" viewBox="0 0 460 463" xmlns="http://www.w3.org/2000/svg">
    <defs>
      <radialGradient id="patternTone" cx="50%" cy="50%" r="70%">
        <stop offset="0" stop-color="var(--pattern-tone)" stop-opacity="0.35"/>
        <stop offset="1" stop-color="var(--pattern-tone)" stop-opacity="0"/>
      </radialGradient>
    </defs>

    <path class="label-edge" d="M4 6 L40 2 L62 7 L95 1 L130 5 L160 0 L198 6 L230 2 L262 6 L300 1 L335 5 L370 0 L405 6 L438 2 L457 5
      L454 40 L459 78 L453 115 L458 150 L452 190 L457 228 L453 265 L458 300 L452 340 L457 378 L453 418 L458 460
      L425 456 L392 462 L356 457 L320 462 L285 456 L250 461 L214 456 L180 462 L145 457 L110 462 L75 456 L40 461 L3 457
      L7 420 L1 382 L6 345 L0 305 L6 268 L1 230 L7 192 L1 155 L6 118 L0 80 L6 42 Z"/>
    <rect class="label-pattern" x="8" y="8" width="444" height="447" role="img" aria-label="Faint scattered cashew nut pattern"/>

    <text class="headline" x="53" y="123" font-size="112" textLength="362" lengthAdjust="spacingAndGlyphs">CASHEWS</text>
    <text class="connector" transform="translate(73 228) rotate(-90)" font-size="30" textLength="78" lengthAdjust="spacingAndGlyphs">med</text>
    <text class="headline" x="75" y="228" font-size="108" textLength="275" lengthAdjust="spacingAndGlyphs">SESAM</text>
    <text class="ampersand" x="350" y="226" font-size="92" textLength="65" lengthAdjust="spacingAndGlyphs">&amp;</text>
    <text class="headline" x="53" y="333" font-size="110" textLength="364" lengthAdjust="spacingAndGlyphs">HONNING</text>

    <g class="ribbon">
      <path class="ribbon-fold" d="M15 392 L60 388 L62 420 L20 428 L32 410 Z"/>
      <path class="ribbon-fold" d="M445 392 L400 388 L398 420 L440 428 L428 410 Z"/>
      <path class="ribbon-band" d="M52 372 Q230 358 408 372 L404 402 Q230 390 56 402 Z"/>
    </g>
    <text class="claims" x="66" y="393" font-size="22" textLength="324" lengthAdjust="spacingAndGlyphs">vegan laktosefri glutenfri</text>

    <text class="maker-line" x="222" y="408" font-size="9" text-anchor="middle">et produckt fra</text>
    <text class="brand-name" x="222" y="428" font-size="16" text-anchor="middle">TYVO</text>
  </svg>
</main>
</body>
</html>
```